Business Card Design

I am a GP with interest in Dermatology and Aesthetic Medicin, performing Botulinum Toxin Type A and Dermal Fillers treatmets in Cosmetic Dermatology clinic.

I am looking for a white colour, good quality white paper card may be of some special texture with black calligraphic writing but easy to read and not to wiggly- professional- looking.

Really appreciate your help.

Milena

Contact Information for Business Card

Cosmetic Dermatology Clinic

Dr Milena Ravitskaya, MBBS, MRCGP, DPD

Tel: 07915 462 170
milena@medpractice-mail.co.uk

```html
<!DOCTYPE html>
<html lang="en">
<head>
<meta charset="utf-8">
<title>Cosmetic Dermatology Clinic – Business Card</title>
<link rel="stylesheet" href="https://fonts.googleapis.com/css2?family=Sofia+Sans+Extra+Condensed:wght@300&display=swap">
<style>
  :root {
    --paper: #ffffff;
    --ink: #111111;
  }
  html, body {
    margin: 0;
    padding: 0;
    width: 791px;
    height: 1200px;
    overflow: hidden;
    background: var(--paper);
  }
  .card {
    position: relative;
    width: 791px;
    height: 1200px;
    background: var(--paper);
    overflow: hidden;
  }
  .divider {
    position: absolute;
    left: 254px;
    top: 710px;
    width: 537px;
    height: 56px;
  }
  .divider-rule {
    position: absolute;
    left: 0;
    right: 0;
    top: 28px;
    height: 3px;
    background: var(--ink);
  }
  .details {
    position: absolute;
    right: 89px;
    top: 772px;
    margin: 0;
    text-align: right;
    font-family: "Sofia Sans Extra Condensed", sans-serif;
    font-weight: 300;
    font-style: normal;
    font-size: 48px;
    line-height: 58px;
    letter-spacing: 2px;
    color: var(--ink);
  }
  .details span {
    display: block;
    white-space: nowrap;
  }
</style>
</head>
<body>
  <main class="card">
    <div class="divider" role="img" aria-label="Flowing wave line leading into a horizontal rule">
      <div class="divider-rule"></div>
    </div>
    <address class="details">
      <span class="clinic-name">Cosmetic Dermatology Clinic</span>
      <span class="doctor-name">Dr Milena Ravitskaya</span>
      <span class="credentials">MBBS, MRCGP, DPD</span>
      <span class="phone">Tel: 07915 462 170</span>
      <span class="email">milena@medpractice-mail.co.uk</span>
    </address>
  </main>
</body>
</html>
```